Website Design Needed for Performance Horse Trading Business

We require a website designed for Pinegallop, a new business which lists top quality performance stock horse bloodlines for sale. Our Australian company caters to the Australian Stock Horse, Quarter Horse and Paint Horse breeds of horse used for performance events such as Camp drafting and Cutting. The website design needs to communicate quality, have a professional look while maintaining a western, rural feel.
Colour schemes that we are looking for are either grey and orange, navy and grey or brown and grey.
The logo for the website has been attached below
Design deliverables are as follows:
-Main Page
-Horses for Sale Page
-Horse Listing Page
-Html & CSS files for pages
MAIN PAGE
----------------
Description: This page is where customers land, search for horses, see premium horses
Elements which need to be included on the main page are
-a horse filter section, allowing customers to search for horse listings by filtering attributes.
-premium listings displaying large photos of horse, price and location.
Horses for Sale PAGE
---------------------------------
Description: This page displays a list of available horses for sale as per the filtered results.
Elements which need to be included on this page are
- a filter panel which allows customers to filter results
- list of horses available for sale
Horse Listing Page
-------------------------------
Description: This page displays all the information about the horse for sale.
Screenshots of the basic program are attached for the Horses for Sale Page and the Horse Listing Page to give an idea of the elements required ONLY and should not be thought of as a design guideline.
Webpage HEADER
-------------------------
The Header section of the website should include login/signup buttons, 'my account' buttons (or links) as well as a featured link/button that says 'Sell Your Horse'
Updates
Thank you all for your designs so far. We would like to see the Sell Your Horse section featured more in the website design to attract customers. This would be as a button or highlighted link that is eye catching in the primary section of the website design of the main page. Perhaps placing it on the right hand side adjacent to the search function lets customers make the mental decision as to whether they are looking to buy or looking to sell when they visit the website. The wording above or near the button would be 'Advertise your horse with us' with the words on the button being 'Create Ad!'.

```html
<!DOCTYPE html>
<html lang="en">
<head>
<meta charset="utf-8">
<title>Pinegallop – Performance Horses</title>
<link rel="stylesheet" href="https://fonts.googleapis.com/css2?family=Hind:wght@300;400;500;600&family=Open+Sans:ital,wght@0,400;0,600;1,400&display=swap">
<style>
  :root{
    --orange:#f0952e;
    --orange-light:#f6ad4e;
    --orange-dark:#e0841e;
    --ink:#222;
    --text:#555;
    --muted:#8a8a8a;
    --line:#dedede;
    --panel:#f2f2f2;
    --footer:#f0f0f0;
    --white:#fff;
    --black:#000;
  }
  *{box-sizing:border-box;margin:0;padding:0}
  html,body{width:936px;height:1200px;overflow:hidden;background:var(--white)}
  body{font-family:"Hind",sans-serif;color:var(--text);position:relative}
  .abs{position:absolute}

  /* header */
  .account-links{right:122px;top:8px;font-size:12px;color:var(--ink);font-family:"Open Sans",sans-serif}
  .account-links span{margin:0 4px}
  .sell-btn{left:716px;top:42px;width:99px;height:24px;background:var(--orange);color:var(--white);
    font-size:12px;line-height:25px;text-align:center;border-radius:2px;font-family:"Open Sans",sans-serif}
  .brand{left:114px;top:22px;display:flex;align-items:center;gap:10px;font-size:34px;font-weight:600;color:var(--ink);letter-spacing:.5px}
  .brand-dot{width:14px;height:14px;border-radius:50%;background:var(--ink)}
  .main-nav{left:118px;top:83px;width:702px;height:38px;background:linear-gradient(var(--orange-light),var(--orange-dark));
    display:flex;align-items:center;padding-left:32px;gap:34px}
  .main-nav a{color:var(--white);text-decoration:none;font-size:14px;font-weight:500;padding-top:2px}

  /* hero */
  .hero-band{left:0;top:121px;width:936px;height:319px;
    background:repeating-linear-gradient(135deg,#f3f3f3 0 2px,#e8e8e8 2px 4px)}
  .hero-photo{left:118px;top:121px;width:702px;height:309px;
    background:linear-gradient(100deg,#8a6a4a 0%,#3b3632 30%,#2c2a29 50%,#6a4a34 75%,#4a3e36 100%)}
  .hero-caption{left:147px;top:222px;width:294px;height:118px;background:rgba(240,149,46,.9);border-radius:2px;padding:18px 19px;color:var(--white)}
  .hero-caption h1{font-size:24px;font-weight:500;line-height:1}
  .hero-caption h2{font-size:17px;font-weight:400;line-height:1.2;margin-top:4px}
  .hero-caption p{font-size:8px;line-height:14px;margin-top:6px;font-family:"Open Sans",sans-serif}
  .slider-dots{left:448px;top:408px;display:flex;gap:3px}
  .slider-dots i{width:9px;height:9px;border-radius:50%;background:#999;display:block}
  .slider-dots i:first-child{background:var(--white)}

  /* featured */
  .section-title{left:116px;top:460px;font-size:20px;font-weight:400;color:var(--ink)}
  .listing{left:114px;width:484px;height:150px;border-bottom:1px solid var(--line)}
  .listing .thumb{position:absolute;left:1px;top:0;width:184px;height:117px}
  .listing .info{position:absolute;left:201px;top:0;width:284px}
  .listing h3{font-size:18px;font-weight:400;color:var(--ink);line-height:1;margin-top:3px}
  .listing p{font-family:"Open Sans",sans-serif;font-size:8.5px;line-height:15px;color:var(--muted);margin-top:9px}
  .listing .meta{font-size:11px;color:var(--text);margin-top:6px}
  .listing .price{font-size:11px;margin-top:1px}
  .listing .price b{font-size:16px;color:var(--orange);font-weight:400}

  /* sidebar */
  .search-box{left:622px;top:464px;width:198px;height:175px;background:var(--panel);border:1px solid #e2e2e2;border-radius:3px;padding:18px 19px}
  .search-box h3{font-size:18px;font-weight:400;color:var(--ink);line-height:1}
  .search-box .sub{font-size:9.5px;color:#aaa;margin-top:3px}
  .field{width:161px;height:20px;background:var(--white);border:1px solid #dadada;font-size:8px;color:var(--muted);
    padding:0 8px;line-height:21px;margin-top:5px;font-family:"Open Sans",sans-serif}
  .search-box .sub+.field{margin-top:9px}
  .search-btn{width:71px;height:20px;background:var(--orange);color:var(--white);font-size:10.5px;font-weight:500;text-align:center;line-height:21px;margin-top:7px}
  .quote{left:623px;top:653px;width:196px;height:157px;background:linear-gradient(var(--orange),var(--orange-dark));padding:25px 20px 0 29px;color:var(--white)}
  .quote p{font-family:"Open Sans",sans-serif;font-style:italic;font-size:8.5px;line-height:15.2px}
  .quote .mark{position:absolute;left:12px;top:14px;font-size:22px;font-family:"Open Sans",sans-serif;opacity:.8}
  .quote-tail{left:652px;top:809px}
  .quote-author{left:651px;top:821px;font-size:9px;line-height:14px;color:var(--ink);font-family:"Open Sans",sans-serif}
  .deals{left:623px;top:865px;width:197px;height:205px;border:1px solid var(--line);border-top:none}
  .deals-head{height:34px;background:var(--black);color:var(--white);font-size:15px;padding:9px 0 0 18px;margin:0 -1px}
  .deal{position:absolute;left:16px;width:170px;height:52px}
  .deal .thumb{position:absolute;left:0;top:0;width:58px;height:50px}
  .deal h4{position:absolute;left:66px;top:-2px;font-size:12px;font-weight:400;color:var(--orange)}
  .deal p{position:absolute;left:66px;top:15px;font-size:7.5px;line-height:13.6px;color:var(--muted);font-family:"Open Sans",sans-serif}

  /* footer */
  .site-footer{left:0;top:1106px;width:936px;height:94px;background:var(--footer);border-top:1px solid #e6e6e6}
  .footer-nav{left:115px;top:1134px;font-size:11px;color:var(--ink)}
  .footer-nav span{margin:0 4px}
  .copyright{left:115px;top:1156px;font-size:9px;color:var(--text);font-family:"Open Sans",sans-serif}
  .social{left:760px;top:1132px;display:flex;gap:6px}
  .social i{width:15px;height:15px;display:block;border-radius:2px}
</style>
</head>
<body>
  <div class="abs account-links">My Account<span>|</span>Login<span>|</span>Sign Up</div>
  <div class="abs brand"><span class="brand-dot"></span>Pinegallop</div>
  <div class="abs sell-btn">Sell Your Horse</div>

  <nav class="abs main-nav">
    <a>HOME</a><a>ABOUT US</a><a>PREMIUM HORSES</a><a>SUPPORT</a><a>TESTIMONIALS</a><a>BLOG</a><a>CONTACT</a>
  </nav>

  <div class="abs hero-band"></div>
  <div class="abs hero-photo" role="img" aria-label="Herd of bay and black horses facing forward"></div>
  <div class="abs hero-caption">
    <h1>Australian Stock Horse</h1>
    <h2>Morbi diam mauris viverra</h2>
    <p>Aiam est nunc venenatis in tristique eu imperdiet ac nisl Cum sociis natoque penatibus et magnis dis parturient</p>
  </div>
  <div class="abs slider-dots"><i></i><i></i><i></i><i></i></div>

  <h2 class="abs section-title">Featured Horses</h2>

  <article class="abs listing" style="top:498px">
    <div class="thumb" role="img" aria-label="Chestnut horse in a field" style="background:linear-gradient(120deg,#c9b48a,#8a4a22 45%,#6a3a1e)"></div>
    <div class="info">
      <h3>Suspendisse quam molestie sed</h3>
      <p>Aiam est nunc venenatis in tristique eu imperdiet ac nisl Cum sociis natoque penatibus et magnis dis parturient montes nascetur ridicu-lus mus In iaculis facilisis massa Etiam eu urna Sed</p>
      <div class="meta">Location:&nbsp; New York</div>
      <div class="price">Price: <b>$5000</b></div>
    </div>
  </article>

  <article class="abs listing" style="top:648px">
    <div class="thumb" role="img" aria-label="Bay horse galloping on a beach" style="background:linear-gradient(180deg,#c8cfcc,#d9d2c2 55%,#cbbfa8)"></div>
    <div class="info">
      <h3>Curabitur iaculis tempus eros</h3>
      <p>Aiam est nunc venenatis in tristique eu imperdiet ac nisl Cum sociis natoque penatibus et magnis dis parturient montes nascetur ridicu-lus mus In iaculis facilisis massa Etiam eu urna Sed</p>
      <div class="meta">Location:&nbsp; New York</div>
      <div class="price">Price: <b>$5000</b></div>
    </div>
  </article>

  <article class="abs listing" style="top:798px">
    <div class="thumb" role="img" aria-label="Rider on a grey horse jumping" style="background:linear-gradient(120deg,#3f6a2a,#7a9a55 50%,#2e4e22)"></div>
    <div class="info">
      <h3>Ut nisi erat fermentum</h3>
      <p>Aiam est nunc venenatis in tristique eu imperdiet ac nisl Cum sociis natoque penatibus et magnis dis parturient montes nascetur ridicu-lus mus In iaculis facilisis massa Etiam eu urna Sed</p>
      <div class="meta">Location:&nbsp; New York</div>
      <div class="price">Price: <b>$5000</b></div>
    </div>
  </article>

  <article class="abs listing" style="top:948px;border-bottom:none">
    <div class="thumb" role="img" aria-label="Rider on a bay horse among trees" style="background:linear-gradient(120deg,#4a7a3a,#8a5a34 55%,#5a3a22)"></div>
    <div class="info">
      <h3>Nunc porta convallis</h3>
      <p>Aiam est nunc venenatis in tristique eu imperdiet ac nisl Cum sociis natoque penatibus et magnis dis parturient montes nascetur ridicu-lus mus In iaculis facilisis massa Etiam eu urna Sed</p>
      <div class="meta">Location:&nbsp; New York</div>
      <div class="price">Price: <b>$5000</b></div>
    </div>
  </article>

  <aside class="abs search-box">
    <h3>Search Horse</h3>
    <div class="sub">Curabitur iaculis tempus eros Curabit</div>
    <div class="field">type word</div>
    <div class="field">Horse Breed</div>
    <div class="field">By Category</div>
    <div class="search-btn">SEARCH</div>
  </aside>

  <blockquote class="abs quote">
    <span class="mark">&ldquo;</span>
    <p>Morbi ornare gravida elit Integer congue augue et malesuada iaculis ipsum dui aliquet felis at cursus magna nisl nec elit Praesent elementum elit at tellus nec ultricies sit amet porttitor mattis enim In massa libero interdum nec in</p>
  </blockquote>
  <svg class="abs quote-tail" width="14" height="8" viewBox="0 0 14 8"><path d="M0 0H14L7 8Z" fill="#e0841e"/></svg>
  <div class="abs quote-author">By Author Name<br>Location, City</div>

  <section class="abs deals">
    <div class="deals-head">Recent Deals</div>
    <div class="deal" style="top:53px">
      <div class="thumb" role="img" aria-label="Horse in a stable" style="background:linear-gradient(120deg,#5a4a3a,#8a7a6a 50%,#3a3028)"></div>
      <h4>Featured Horse</h4>
      <p>venenatis in tristique eu<br>imperdiet ac nisl Cum sociis<br>natoque penatibus</p>
    </div>
    <div class="deal" style="top:121px">
      <div class="thumb" role="img" aria-label="Chestnut horse against blue sky" style="background:linear-gradient(120deg,#8ab8dc,#9a5a30 55%,#6a3a1e)"></div>
      <h4>Featured Horse</h4>
      <p>venenatis in tristique eu<br>imperdiet ac nisl Cum sociis<br>natoque penatibus</p>
    </div>
  </section>

  <footer class="abs site-footer"></footer>
  <div class="abs footer-nav">HOME<span>|</span>ABOUT US<span>|</span>PREMIUM HORSES<span>|</span>SUPPORT<span>|</span>TESTIMONIALS<span>|</span>BLOG<span>|</span>CONTACT</div>
  <div class="abs copyright">© 2014 Company Name&nbsp; All right reserved&nbsp; Term of Use</div>
  <div class="abs social" aria-label="Social links">
    <i style="background:#3b5a98"></i><i style="background:#5bb8e6"></i><i style="background:#1a78b4"></i>
  </div>
</body>
</html>
```